Creative Web Design - Intl Market Research Company

We need an innovative web design for an emerging company into the international market research marketplace.

The company, Halvenor Associates, is a Trade, Investment, and Market Research company. Halvenor offers domestic and international companies increased success in the U.S. marketplace by providing a variety of services. (seen on attached brochure)

The website should be cutting edge and creative while having an easy navigation. The color is not fixed and attached logo is not finalized, feel free to post anything from conservative to progressive options. Keep in mind target customers are domestic and international businesses looking to emerge/improve in the U.S. marketplace.

Additional Company information is located in the attached documentation. The documentation is outdated & winner will have priority standing for our next projects.(logo & document re-design)

I have received a few e-mail requests and have updated the status to guaranteed payment.

Thanks!

Target Market(s)

Any company, foreign and domestic, looking to introduce their product into the U.S. marketplace.

Industry/Entity Type

Market Research

Requirements
Must have
• Easy Navigation
Should not have
• Too many buttons
Difficult navigation
Excessive Typography

```html
<!DOCTYPE html>
<html lang="en">
<head>
<meta charset="utf-8">
<title>Halvenor Associates</title>
<link rel="stylesheet" href="https://fonts.googleapis.com/css2?family=Source+Sans+3:wght@400;600;700&display=swap">
<style>
:root{
  --maroon:#7a0a0a;
  --maroon-dark:#2e0404;
  --gold:#9c6a0c;
  --gold-light:#ab7c1c;
  --gold-text:#5a3c05;
  --stripe:#dde3e1;
  --ink:#4a4a4a;
  --meta:#8a8a8a;
  --tab:#f1efec;
  --font:"Source Sans 3",Arial,sans-serif;
}
*{margin:0;padding:0;box-sizing:border-box}
html,body{width:953px;height:1200px;overflow:hidden;background:#fff;font-family:var(--font);color:var(--ink)}
.page{position:relative;width:953px;height:1200px}
.abs{position:absolute}
.top-rule{left:0;top:13px;width:953px;height:1px;background:#e6e6e6}
.lang{right:28px;top:22px;display:flex;align-items:center;gap:7px;font-size:10.5px;color:#666}
.lang svg{display:block}
.brand{left:52px;top:170px;font-size:36px;font-weight:700;color:var(--gold);letter-spacing:.5px;font-variant:small-caps}
.nav{left:434px;top:174px;display:flex;gap:2px}
.nav a{display:block;width:121px;height:47px;line-height:48px;text-align:center;font-size:18px;font-weight:700;color:var(--maroon);text-decoration:none;background:linear-gradient(#f7f6f4,#e9e6e1)}
.nav a.active{color:#fff;background:linear-gradient(#8f1408,#6b0a05)}
.hero{left:0;top:221px;width:953px;height:262px;background:linear-gradient(160deg,var(--gold),var(--gold-light))}
.hero-photo{left:28px;top:11px;width:420px;height:240px;background:linear-gradient(120deg,#c9d6e6,#eef2f8 55%,#a9bcd3);box-shadow:1px 1px 2px rgba(0,0,0,.35)}
.hero-title{left:503px;top:32px;font-size:29px;font-weight:700;color:#fff;font-variant:small-caps;text-shadow:1px 1px 1px rgba(0,0,0,.35)}
.hero-text{left:503px;top:87px;width:420px;font-size:17px;line-height:22.5px;color:#fff}
.btn{display:block;width:140px;height:28px;border-radius:14px;background:linear-gradient(#fff,#e4e2de);box-shadow:2px 2px 2px rgba(0,0,0,.35);text-align:center;line-height:28px;font-size:16px;font-weight:700;color:var(--gold-text);text-decoration:none}
.hero .btn{position:absolute;left:503px;top:194px}
.stripe{left:0;top:483px;width:953px;height:10px;background:var(--stripe)}
h2{font-size:24px;font-weight:400;color:var(--maroon);line-height:1}
.meta{font-size:10.5px;color:var(--meta)}
.meta span{margin:0 7px}
.post{width:430px;height:160px}
.post h2{position:absolute;left:0;top:0}
.post .meta{position:absolute;left:2px;top:36px}
.post-photo{position:absolute;left:0;top:56px;width:187px;height:94px;border:1px solid #cfcfcf;background:linear-gradient(#f4f4f4,#dcdde2)}
.post p{position:absolute;left:230px;top:58px;width:200px;font-size:12.5px;line-height:18px}
.post .btn{position:absolute;left:230px;top:118px}
.article{left:28px;top:750px;width:540px}
.article .meta{margin-top:22px}
.article p{font-size:12.3px;line-height:17.8px;margin-top:17px;letter-spacing:.1px}
.article p:first-of-type{margin-top:18px}
.link{display:inline-block;font-size:12.5px;color:var(--gold-text);text-decoration:none}
.article .link{margin-top:8px}
.aside{left:621px;top:750px;width:300px}
.feature{position:absolute;left:0;width:300px}
.feature svg{position:absolute;left:7px;top:0}
.feature h3{position:absolute;left:67px;top:0;font-size:12.5px;font-weight:400;color:#111;letter-spacing:.2px}
.feature p{position:absolute;left:67px;top:24px;font-size:12.3px;line-height:18px;width:200px}
.feature .link{position:absolute;left:67px;top:70px}
.footer{left:0;top:1164px;width:929px;height:36px;background:var(--maroon-dark);font-size:10.5px;color:#a88;padding:6px 0 0 28px}
</style>
</head>
<body>
<div class="page">
  <div class="abs top-rule"></div>

  <div class="abs lang">Choose language
    <svg width="15" height="10" viewBox="0 0 15 10"><rect width="15" height="10" fill="#1f3a8a"/><path d="M0 0L15 10M15 0L0 10" stroke="#fff" stroke-width="2"/><rect x="6" width="3" height="10" fill="#fff"/><rect y="3.5" width="15" height="3" fill="#fff"/><rect x="6.8" width="1.4" height="10" fill="#c8102e"/><rect y="4.3" width="15" height="1.4" fill="#c8102e"/></svg>
    <svg width="15" height="10" viewBox="0 0 15 10"><rect width="15" height="3.4" fill="#111"/><rect y="3.3" width="15" height="3.4" fill="#d00"/><rect y="6.6" width="15" height="3.4" fill="#fc0"/></svg>
    <svg width="15" height="10" viewBox="0 0 15 10"><rect width="5" height="10" fill="#1f3a8a"/><rect x="5" width="5" height="10" fill="#fff"/><rect x="10" width="5" height="10" fill="#d22"/></svg>
    <svg width="15" height="10" viewBox="0 0 15 10"><rect width="5" height="10" fill="#1a9a3c"/><rect x="5" width="5" height="10" fill="#fff"/><rect x="10" width="5" height="10" fill="#d22"/></svg>
  </div>

  <div class="abs brand">Halvenor Associates</div>

  <nav class="abs nav">
    <a href="#" class="active">Home</a>
    <a href="#">Projects</a>
    <a href="#">Services</a>
    <a href="#">Contact</a>
  </nav>

  <section class="abs hero">
    <div class="abs hero-photo" role="img" aria-label="Photo of business people walking through a bright modern lobby"></div>
    <h1 class="abs hero-title">Main Title Goes Here</h1>
    <p class="abs hero-text">Vocent labores atomorum per an, ei sed voluptua efficiantur. Sit nobis efficiendi in. Ex eruditi imperdiet adipiscing vis, ius natum munere dolorem ne, ius</p>
    <a href="#" class="btn">Read more</a>
  </section>
  <div class="abs stripe"></div>

  <article class="abs post" style="left:28px;top:533px">
    <h2>Habemus scaevola dicant legimus</h2>
    <div class="meta">Author: Admin<span>|</span>15 July 2013<span>|</span>Comments (32)</div>
    <div class="post-photo" role="img" aria-label="Photo of a business team standing in a row"></div>
    <p>In quaeque eripuit vivendo qui. Eu quo postulant constituto intellegebat, cu fugit clita</p>
    <a href="#" class="btn">Read more</a>
  </article>

  <article class="abs post" style="left:504px;top:533px">
    <h2>Habemus scaevola eam dicant</h2>
    <div class="meta">Author: Admin<span>|</span>15 July 2013<span>|</span>Comments (32)</div>
    <div class="post-photo" role="img" aria-label="Photo of business people in dark suits standing together"></div>
    <p>In quaeque eripuit vivendo qui. Eu quo postulant constituto intellegebat, cu fugit clita</p>
    <a href="#" class="btn">Read more</a>
  </article>

  <article class="abs article">
    <h2>Habemus scaevola dicant legimus</h2>
    <div class="meta">Author: Admin<span>|</span>15 July 2013<span>|</span>Comments (32)</div>
    <p>In quaeque eripuit vivendo qui. Eu quo postulant constituto intellegebat, cu fugit clita liberavisse nec, has quando delectus ut. Paulo elaboraret ex ius. Inani errem no sea, petentium complectitur vituperatoribus eu vim. Pri summo copiosae suscipiantur an.</p>
    <p>Ex efficiendi omittantur est, mutat laboramus consetetur ex has. Cu qui nusquam democritum interpretaris, mea eu docendi deseruisse sententiae. Vocent delectus scribentur cum et. Has et autem interpretaris. Ut vel alia unum.</p>
    <p>Mucius dolorem vivendo ea mel. Nam at everti vocibus convenire. Nam ad agam nonumes. Habeo delicata per no, an adhuc cetero intellegam cum. Tation principes constituam duo ne, his posidonium voluptatibus eu.</p>
    <p>Quod iudicabit id pro, ferri debitis in vix. Sed ea apeirian periculis disputationi. Nullam electram principes pri id. Ferri petentium assentior ius ut. Quis ornatus te est, melius iudicabit periculis et sea. In eos quem tota vidit, hinc duis consetetur vim ea, duo ne nullam euismod.</p>
    <a href="#" class="link">Read more</a>
  </article>

  <aside class="abs aside">
    <h2>Movet Detracto</h2>
    <div class="feature" style="top:56px">
      <svg width="38" height="38" viewBox="0 0 38 38"><circle cx="24" cy="14" r="10" fill="none" stroke="#111" stroke-width="2.5"/><path d="M24 9v10M19 14h10" stroke="#111" stroke-width="2.2"/><path d="M17 21L5 33" stroke="#111" stroke-width="5" stroke-linecap="round"/></svg>
      <h3>SMALL TITLE GOES HERE</h3>
      <p>In quaeque eripuit vivendo qui. Eu quo postulant constituto</p>
      <a href="#" class="link">Read more</a>
    </div>
    <div class="feature" style="top:175px">
      <svg width="38" height="38" viewBox="0 0 38 38"><circle cx="19" cy="19" r="14" fill="#111"/></svg>
      <h3>SMALL TITLE GOES HERE</h3>
      <p>In quaeque eripuit vivendo qui. Eu quo postulant constituto</p>
      <a href="#" class="link">Read more</a>
    </div>
    <div class="feature" style="top:294px">
      <svg width="38" height="46" viewBox="0 0 38 46"><path d="M19 4a8 8 0 0 1 8 8M19 0a12 12 0 0 1 12 12" fill="none" stroke="#111" stroke-width="2"/><circle cx="17" cy="16" r="3" fill="#111"/><path d="M15.5 18h3v10h-3z" fill="#111"/><path d="M5 44c0-9 6-16 12-16s12 7 12 16z" fill="#111"/></svg>
      <h3>SMALL TITLE GOES HERE</h3>
      <p>In quaeque eripuit vivendo qui. Eu quo postulant constituto</p>
      <a href="#" class="link">Read more</a>
    </div>
  </aside>

  <footer class="abs footer">Copyright © Halvenor Associates</footer>
</div>
</body>
</html>
```